Shopify Web-Page "Kids-LoomNestery

We are building a new business in Switzerland offering premium sewing holiday camps for kids aged 9–14. In enclosed brief outlines our requirements for a complete Shopify homepage design and a multilingual logo creation.
Domains: kids-loomnest.example ; kids-nidotelaio.example ; kids-webnest.example

Project Overview
We are looking for:
1. A modern, fully designed Shopify homepage in English using standard Shopify content blocks (no custom coding), which we can later update ourselves. Supporting Multilanguage (EN, German, Italian).

2. A logo design that includes the brand identity and communicates our multilingual, creative, and child-focused positioning.

All details in enclosed

```html
<!DOCTYPE html>
<html lang="en">
<head>
<meta charset="utf-8">
<title>Kids LoomNestery Sewing</title>
<link href="https://fonts.googleapis.com/css2?family=Poppins:wght@400;500;600;700&display=swap" rel="stylesheet">
<style>
:root{--pink:#c8094d;--blue:#0b9fc6;--yellow:#f5b50a;--ink:#1f1f2b;--text:#555;--line:#e3e3e3;--white:#fff}
*{box-sizing:border-box;margin:0;padding:0}
html,body{width:1200px;height:3789px;overflow:hidden}
body{font-family:'Poppins',sans-serif;color:var(--ink);background:var(--white);position:relative}
.abs{position:absolute}
.pink{color:var(--pink)}.blue{color:var(--blue)}.yellow{color:var(--yellow)}
.btn{position:absolute;background:var(--pink);color:#fff;font-weight:700;font-size:15px;border-radius:30px;display:flex;align-items:center;justify-content:center;text-transform:uppercase}
.brand{left:0;width:1200px;top:26px;display:flex;justify-content:center;align-items:center;gap:12px;font-size:24px;font-weight:600;color:var(--pink)}
.brand-dot{width:34px;height:34px;border-radius:50%;background:var(--pink)}
.nav{top:82px;left:280px;display:flex;font-size:14px;font-weight:500}
.nav span{padding:4px 16px;margin-right:20px}
.nav .active{background:var(--yellow);border-radius:14px}
.hero{top:119px;left:0;width:1200px;height:600px;background:linear-gradient(100deg,#e6e6e6 0%,#d9d5d2 45%,#c9b7aa 70%,#ddd 100%)}
.hero-card{top:262px;left:144px;width:519px;height:286px;background:#fff;border-radius:18px;padding:32px 39px}
.hero-card h1{font-size:35px;line-height:48px;font-weight:600}
.hero-card p{font-size:14px;line-height:27px;color:#1e3c6e;margin-top:12px}
.section-title{font-size:30px;font-weight:600;text-align:center;width:1200px;left:0}
.step{width:260px;text-align:center}
.step .num{width:40px;height:40px;border-radius:50%;color:#fff;font-weight:600;font-size:17px;display:flex;align-items:center;justify-content:center;margin:0 auto}
.step .icon{width:90px;height:90px;margin:20px auto 0;border-radius:8px}
.step h3{font-size:15px;font-weight:500;margin-top:24px}
.step p{font-size:13px;line-height:23px;color:#444;margin-top:8px}
.card{background:#fff;border-radius:16px;box-shadow:0 4px 24px rgba(0,0,0,.08);overflow:hidden}
.card h2{font-size:30px;font-weight:600;line-height:40px}
.card p{font-size:14px;line-height:24px;color:var(--text)}
.photo{position:absolute}
.why-list{list-style:none;margin-top:12px}
.why-list li{font-size:13px;line-height:24px;color:#555;padding-left:28px;position:relative;white-space:nowrap;letter-spacing:-.1px}
.why-list li::before{content:"";position:absolute;left:2px;top:8px;width:10px;height:10px;border-radius:50%;background:var(--yellow)}
.camp{border-radius:10px;padding:15px}
.camp .pic{height:280px;border-radius:8px}
.camp h3{font-size:17px;font-weight:500;text-align:center;margin-top:22px}
.reserve{top:2458px;left:0;width:1200px;height:319px;background:linear-gradient(90deg,#0aa0c8,#0f93bd 50%,#0aa0c8)}
.faq-item{left:144px;width:911px;border-bottom:1px solid var(--line)}
.faq-q{display:flex;align-items:center;font-size:16px;height:46px}
.faq-q .n{width:26px;height:26px;border-radius:50%;color:#fff;font-size:12px;font-weight:600;display:flex;align-items:center;justify-content:center;margin-right:22px}
.faq-q .t{flex:1}
.news{top:3319px;left:0;width:1200px;height:470px;background:var(--pink);color:#fff}
.foot-col h4{font-size:15px;font-weight:500;margin-bottom:14px}
.foot-col div{font-size:14px;line-height:27px;display:flex;align-items:center;gap:12px}
</style>
</head>
<body>
<header>
  <div class="abs brand"><span class="brand-dot"></span>Kids LoomNestery Sewing</div>
  <nav class="abs nav"><span class="active">HOME</span><span>ABOUT</span><span>WHY CHOOSE US?</span><span>FAQS</span><span>CONTACT</span><span>ENG ▾</span></nav>
</header>

<section class="abs hero" role="img" aria-label="Mother and daughter sewing together at a white sewing machine"></section>
<div class="abs hero-card">
  <h1>The <span class="blue">Most</span> <span class="yellow">Fun</span> They’ll<br>Have All <span class="pink">Year!</span></h1>
  <p>Lorem ipsum dolor sit amet, consectetur adipiscing elit, sed do eiusmod tempor incididunt ut labore</p>
  <div class="btn" style="left:39px;top:206px;width:177px;height:48px">Book Now</div>
</div>

<h2 class="abs section-title" style="top:794px"><span class="blue">How</span> The <span class="pink">Camp</span> Works</h2>
<svg class="abs" style="left:68px;top:1007px" width="20" height="26"><path d="M14 3 4 13l10 10" fill="none" stroke="#222" stroke-width="2.5"/></svg>
<svg class="abs" style="left:1112px;top:1007px" width="20" height="26"><path d="M6 3l10 10L6 23" fill="none" stroke="#222" stroke-width="2.5"/></svg>
<div class="abs step" style="left:149px;top:874px"><div class="num" style="background:var(--blue)">01</div><div class="icon" role="img" aria-label="Clipboard checklist illustration" style="background:#f2d9a6"></div><h3>PROJECT SELECTION</h3><p>Your child chooses their own model based on previously produced clothing items and sewing patterns.</p></div>
<div class="abs step" style="left:477px;top:874px"><div class="num" style="background:var(--yellow)">02</div><div class="icon" role="img" aria-label="Stacked fabric swatches illustration" style="background:linear-gradient(135deg,#f5c20a,#e8457a,#1aa6d8)"></div><h3>FABRIC SELECTION</h3><p>High-quality fabrics are available.</p></div>
<div class="abs step" style="left:806px;top:874px"><div class="num" style="background:var(--pink)">03</div><div class="icon" role="img" aria-label="Sewing machine illustration" style="background:linear-gradient(160deg,#3aa0e0,#9fd3f0)"></div><h3>SEWING MACHINE</h3><p>Operation Learn how to use a sewing machine</p></div>

<div class="abs card" style="left:144px;top:1204px;width:911px;height:323px">
  <div class="abs" style="left:47px;top:44px;width:390px">
    <h2><span class="blue">About</span> Kids <span class="yellow">LoomNestery</span><br><span class="pink">Sewing</span></h2>
    <p style="margin-top:16px">Lorem ipsum dolor sit amet, consectetur adipiscing elit, sed do eiusmod tempor incididunt ut labore et dolore magna aliqua.enim ipsam</p>
  </div>
  <div class="btn" style="left:47px;top:239px;width:176px;height:47px">Learn More</div>
  <div class="photo" role="img" aria-label="Girl and woman working at a sewing machine in a bright room" style="left:456px;top:0;width:455px;height:323px;background:linear-gradient(120deg,#d8d2cc,#efe9e4 50%,#cbb9aa)"></div>
</div>

<div class="abs card" style="left:144px;top:1588px;width:911px;height:363px">
  <div class="photo" role="img" aria-label="Group of children sewing with an instructor in a workshop" style="left:0;top:0;width:373px;height:363px;background:linear-gradient(140deg,#c9b39a,#e6ddd2 50%,#a89380)"></div>
  <div class="abs" style="left:416px;top:44px;width:480px">
    <h2><span class="pink">Why</span> <span class="blue">Parents</span> Choose <span class="yellow">Us</span></h2>
    <ul class="why-list">
      <li>Small groups &amp; personalized attention</li>
      <li>Multilingual supervision (DE / EN / IT)</li>
      <li>High-quality fabrics &amp; top-quality sewing machines (Loomwell)</li>
      <li>Encouragement of creativity, self-confidence, and fine motor skills</li>
      <li>Safe, loving environment in Zurich, various places easy to reach</li>
      <li>Pick-up Service from the Main-Station</li>
    </ul>
  </div>
  <div class="btn" style="left:416px;top:270px;width:176px;height:47px">Learn More</div>
</div>

<div class="abs camp" style="left:144px;top:2021px;width:443px;height:359px;border:1.5px solid #8fd0e3">
  <div class="pic" role="img" aria-label="Children cutting purple fabric with a teacher" style="background:linear-gradient(180deg,#e7e2da,#c9a0e0 70%,#9b52d6)"></div>
  <h3>SPRING CAMPS</h3>
</div>
<div class="abs camp" style="left:612px;top:2021px;width:442px;height:359px;background:var(--pink);color:#fff">
  <div class="pic" role="img" aria-label="Teacher helping a girl at a sewing machine" style="background:linear-gradient(120deg,#cfd9de,#f2f2f0 50%,#bcd6e6)"></div>
  <h3>SUMMER CAMPS</h3>
</div>

<section class="abs reserve" role="img" aria-label="Blue tinted photo of children at camp"></section>
<div class="abs" style="top:2535px;left:0;width:1200px;text-align:center;color:#fff">
  <h2 style="font-size:31px;font-weight:600">Reserve Now for the Best Holiday Ever!</h2>
  <p style="font-size:14px;line-height:24px;margin:20px auto 0;width:900px">Lorem ipsum dolor sit amet, consectetur adipiscing elit, sed do eiusmod tempor incididunt ut labore et dolore magna aliqua.enim ipsam Ut enim ad minim veniam, quis nostrud exercitation ullamco laboris nisi ut aliquip</p>
</div>
<div class="btn" style="left:512px;top:2671px;width:176px;height:47px">Book Now</div>

<h2 class="abs" style="left:144px;top:2838px;font-size:30px;font-weight:600"><span class="pink">Frequently</span> <span class="yellow">Asked</span> Questions</h2>
<div class="abs faq-item" style="top:2910px"><div class="faq-q"><span class="n" style="background:var(--blue)">01</span><span class="t">Does my child need any prior knowledge?</span><svg width="18" height="18"><circle cx="9" cy="9" r="9" fill="#0b9fc6"/><path d="M9 4v10M4 9h10" stroke="#fff" stroke-width="2"/></svg></div></div>
<div class="abs faq-item" style="top:2973px;padding-bottom:18px"><div class="faq-q"><span class="n" style="background:var(--yellow)">02</span><span class="t">How does the pick-up service work?</span><svg width="18" height="18"><circle cx="9" cy="9" r="9" fill="#f5b50a"/><path d="M4 9h10" stroke="#fff" stroke-width="2"/></svg></div>
<p style="font-size:13px;line-height:23px;color:#555">Lorem ipsum dolor sit amet, consectetur adipiscing elit, sed do eiusmod tempor incididunt ut labore et dolore magna aliqua. Ut enim ad minim veniam, quis nostrud exercitation ullamco laboris nisi ut aliquip ex ea commodo consequat. Duis aute iru dolor in reprehenderit in voluptate velit esse cillum dolore eu fugiat nulla pariatur. Excepteur sint occaecat cupidatat non proident.</p></div>
<div class="abs faq-item" style="top:3121px"><div class="faq-q"><span class="n" style="background:var(--blue)">03</span><span class="t">How many items of clothing are produced?</span><svg width="18" height="18"><circle cx="9" cy="9" r="9" fill="#0b9fc6"/><path d="M9 4v10M4 9h10" stroke="#fff" stroke-width="2"/></svg></div></div>
<div class="btn" style="left:496px;top:3208px;width:208px;height:47px">More Questions</div>

<footer class="abs news">
  <h2 style="position:absolute;top:50px;width:1200px;text-align:center;font-size:34px;font-weight:600">Sign Up To Our Newsletter</h2>
  <p style="position:absolute;top:108px;width:1200px;text-align:center;font-size:14px;font-weight:500">Duis aute irure dolor in reprehenderit in voluptate</p>
  <div style="position:absolute;left:383px;top:149px;width:434px;height:46px;border:1.5px solid #fff;border-radius:24px;display:flex;align-items:center;padding:0 20px;font-size:13px;justify-content:space-between"><span>Enter Your Email</span><svg width="18" height="12"><path d="M1 6h15M11 1l5 5-5 5" fill="none" stroke="#fff" stroke-width="1.5"/></svg></div>
  <div class="abs foot-col" style="left:144px;top:240px"><h4>QUICK LINKS</h4><div>Home</div><div>About</div><div>Why Chose Us?</div><div>FAQS</div><div>Contact</div></div>
  <div class="abs foot-col" style="left:478px;top:243px"><h4>CONNECT WITH US</h4>
    <div><svg width="10" height="10"><circle cx="5" cy="5" r="4" fill="#fff"/></svg>Friendbook</div>
    <div><svg width="10" height="10"><circle cx="5" cy="5" r="4" fill="#fff"/></svg>Linkpro</div>
    <div><svg width="10" height="10"><circle cx="5" cy="5" r="4" fill="#fff"/></svg>Chirper</div>
    <div><svg width="10" height="10"><circle cx="5" cy="5" r="4" fill="#fff"/></svg>Snapgram</div>
    <div><svg width="10" height="10"><circle cx="5" cy="5" r="4" fill="#fff"/></svg>Pinboard</div></div>
  <div class="abs foot-col" style="left:833px;top:243px"><h4>CONTACT DETAILS</h4>
    <div><svg width="14" height="14"><path d="M3 1l3 3-2 2c1 2 2 3 4 4l2-2 3 3-2 2C6 13 1 8 1 3z" fill="#fff"/></svg>+1-555-010-2040</div>
    <div><svg width="14" height="12"><rect x="1" y="1" width="12" height="10" fill="#fff"/><path d="M1 1l6 5 6-5" fill="none" stroke="#c8094d"/></svg>info@kids-loomnest.example</div>
    <div><svg width="14" height="16"><path d="M7 1a5 5 0 0 1 5 5c0 4-5 9-5 9S2 10 2 6a5 5 0 0 1 5-5z" fill="#fff"/><circle cx="7" cy="6" r="2" fill="#c8094d"/></svg>Lorem ipsum dolor 12354 , SW</div></div>
  <div style="position:absolute;left:144px;top:418px;width:911px;border-top:1px solid rgba(255,255,255,.4)"></div>
  <p style="position:absolute;top:434px;width:1200px;text-align:center;font-size:13px">Copyright© 2025 Kids LoomNestery Sewing &nbsp;|&nbsp; All Rights Reserved</p>
</footer>
</body>
</html>
```